Business Card for premium dental clinic

We are a premium dental clinic based in Brasov, Romania with more than 15 year on the market, providing quality dental treatment made by a team of more specialized dentists, working with modern equipment as a solution to beautiful and healthy teeth.

Our current logo for the clinic use 2 square with colors black and gold - dr Corbescu - studio, using family fonts Bodoni, Myriad Pro and Segoe Print.
Depending on the printing we used some gold CMYK background or gold foil picture background or a gold gradient.
We want a business card:
- eye catching business card
- distinguished business card
- premium design
- to keep the color scheme of black and gold
- to attract the customers to spent time reading the information
- modern concept

```html
<!DOCTYPE html>
<html lang="ro">
<head>
<meta charset="utf-8">
<title>Dr. Corbescu Studio – business card</title>
<link rel="stylesheet" href="https://fonts.googleapis.com/css2?family=Open+Sans:wght@400;600;700&family=PT+Sans:wght@400;700&display=swap">
<style>
  :root {
    --bg: #d9d9db;
    --black: #0b0b0b;
    --white: #ffffff;
    --gold-dark: #a8740f;
    --gold-mid: #d9a520;
    --gold-light: #f7dc6a;
    --gold-pale: #fff1a8;
    --gold-text: #e0ab2a;
    --frame: linear-gradient(100deg, var(--gold-dark) 0%, var(--gold-light) 22%, var(--gold-mid) 45%, var(--gold-pale) 62%, var(--gold-dark) 82%, var(--gold-light) 100%);
  }
  * { box-sizing: border-box; margin: 0; padding: 0; }
  html, body { width: 1200px; height: 800px; overflow: hidden; }
  body {
    background: var(--bg);
    position: relative;
    font-family: "PT Sans", "Open Sans", sans-serif;
  }
  .card {
    position: absolute;
    width: 560px;
    height: 320px;
    box-shadow: 0 6px 18px rgba(0,0,0,.25);
  }

  /* Front */
  .card-front { left: 500px; top: 50px; background: var(--frame); padding: 18px; }
  .front-inner {
    position: relative;
    width: 100%; height: 100%;
    border: 3px solid var(--white);
    display: flex;
    overflow: hidden;
  }
  .gold-foil {
    width: 56%;
    height: 100%;
    background:
      radial-gradient(circle at 30% 30%, var(--gold-pale) 0%, transparent 45%),
      radial-gradient(circle at 75% 75%, var(--gold-light) 0%, transparent 50%),
      linear-gradient(135deg, var(--gold-mid), var(--gold-light) 50%, var(--gold-mid));
  }
  .black-panel { flex: 1; background: var(--black); position: relative; }
  .name-label {
    position: absolute;
    left: 42px; top: 82px;
    width: 252px; height: 62px;
    background: var(--white);
    display: flex; align-items: center; justify-content: center;
  }
  .name-label span {
    font-family: "Open Sans", sans-serif;
    font-weight: 400;
    font-size: 38px;
    color: var(--black);
    letter-spacing: -.5px;
  }
  .tagline {
    position: absolute;
    right: 12px; bottom: 8px;
    font-family: "Open Sans", sans-serif;
    font-weight: 700;
    font-size: 27px;
    color: var(--white);
  }

  /* Back */
  .card-back { left: 140px; top: 430px; background: var(--black); }
  .gold-band {
    position: absolute;
    left: 0; top: 88px;
    width: 300px; height: 122px;
    background: linear-gradient(160deg, var(--gold-light) 0%, var(--gold-mid) 35%, var(--gold-pale) 55%, var(--gold-dark) 100%);
    border: 3px solid var(--white);
    border-left: none;
    text-align: right;
    padding: 12px 22px 0 0;
    font-family: "PT Sans", sans-serif;
    font-size: 36px;
    line-height: 40px;
    color: var(--black);
  }
  .contact {
    position: absolute;
    left: 318px; top: 100px;
    color: var(--white);
    font-size: 15px;
    line-height: 19px;
  }
  .address { margin-bottom: 10px; }
  .contact-list { list-style: none; }
  .contact-list li { display: flex; align-items: center; gap: 8px; }
  .contact-list svg { width: 13px; height: 13px; flex: none; }
</style>
</head>
<body>

  <section class="card card-front" aria-label="Card front">
    <div class="front-inner">
      <div class="gold-foil" role="img" aria-label="Crumpled gold foil texture"></div>
      <div class="black-panel"></div>
      <div class="name-label"><span>dr. corbescu</span></div>
      <p class="tagline">dental clinic</p>
    </div>
  </section>

  <section class="card card-back" aria-label="Card back">
    <div class="gold-band">Dr. Corbescu<br>Studio</div>
    <div class="contact">
      <p class="address">strada 21 Aprilie nr 4<br>Brasov, Romania 500120</p>
      <ul class="contact-list">
        <li>
          <svg viewBox="0 0 14 14" fill="none" stroke="var(--gold-text)" stroke-width="1.4"><rect x="3.5" y="1" width="7" height="12" rx="1"/><line x1="6" y1="11" x2="8" y2="11"/></svg>
          +40 700 318 412
        </li>
        <li>
          <svg viewBox="0 0 14 14" fill="var(--gold-text)"><path d="M3 1l2.5 3-1.3 1.5c.8 1.8 2.2 3.2 4 4L9.7 8.2 13 10.5 11.5 13C6 12.5 1.5 8 1 2.5z"/></svg>
          +40 268 520 305
        </li>
        <li>
          <svg viewBox="0 0 14 14" fill="none" stroke="var(--gold-text)" stroke-width="1.4"><rect x="1" y="3" width="12" height="8"/><polyline points="1,3 7,8 13,3"/></svg>
          info@drcorbescu.ro
        </li>
        <li>
          <svg viewBox="0 0 14 14" fill="none" stroke="var(--gold-text)" stroke-width="1.2"><circle cx="7" cy="7" r="6"/><ellipse cx="7" cy="7" rx="2.6" ry="6"/><line x1="1" y1="7" x2="13" y2="7"/></svg>
          www.drcorbescu.ro
        </li>
      </ul>
    </div>
  </section>

</body>
</html>
```